Wanderlark Gin - Bottle Label for a craft Gin about to be launched on the world from New Zealand

We are a start up craft distillery in New Zealand. We have developed a wonderful Gin using our own grain spirit and both traditional and New Zealand native botanicals (Manuka to be specific), chosen our bottle and the name "Wanderlark" and done a bit of amateur label design and now we are looking for someone to make it great.

Feel free to change up our amateur concept but give us something that will pop from the back bar and scream authenticity, craft and individuality.

The attached files give you the specifications of the bottle, our current concept for a Wanderlark label and an earlier concept drawing that gives an idea of where we are thinking the two labels should go on the front of the bottle.

Thanks, we look forward to your ideas!!

Target Market(s)

High end and craft Gin drinkers. Hipsters and cocktail barflys and their bar tenders and bar owners

Font styles to use
Serif
Sans Serif
Decorative
Script

Requirements
Must have
• Attractive individuality
Nice to have
• Coolness
Should not have
• Uncoolness

```html
<!DOCTYPE html>
<html lang="en">
<head>
<meta charset="utf-8">
<title>Wanderlark Gin – Recipe #3 Labels</title>
<link rel="stylesheet" href="https://fonts.googleapis.com/css2?family=Jost:wght@400;500&family=Antonio:wght@300;400&display=swap">
<style>
  :root {
    --paper: #ffffff;
    --frame: #1a1a1a;
    --peach: #f3ab6f;
    --ink: #111111;
    --leaf: #0f9a45;
    --gold-light: #fff6d8;
    --gold-mid: #e6c45e;
    --gold-deep: #7a5f1c;
    --gold-dark: #0c0a05;
  }
  html, body {
    margin: 0;
    padding: 0;
    overflow: hidden;
    background: var(--paper);
  }
  .canvas {
    width: 1200px;
    height: 1199px;
    position: relative;
    background: var(--paper);
    box-sizing: border-box;
    border: 1px solid var(--frame);
  }
  .artwork {
    display: block;
    width: 100%;
    height: 100%;
  }
  .recipe-title {
    font-family: "Jost", sans-serif;
    font-weight: 500;
    font-size: 58px;
    letter-spacing: 27px;
    fill: var(--ink);
  }
  .recipe-title .hash { fill: var(--paper); }
  .tasting-note {
    font-family: "Antonio", sans-serif;
    font-weight: 300;
    font-size: 26px;
    letter-spacing: 4px;
    fill: var(--ink);
  }
  .proof {
    font-family: "Jost", sans-serif;
    font-size: 36px;
    letter-spacing: 1px;
    fill: var(--ink);
  }
  .abv-figure {
    font-family: "Jost", sans-serif;
    font-weight: 500;
    font-size: 60px;
    fill: var(--ink);
  }
  .abv-caption {
    font-family: "Jost", sans-serif;
    font-size: 27px;
    letter-spacing: 1px;
    fill: var(--ink);
  }
  .brand-name {
    font-family: "Jost", sans-serif;
    font-weight: 500;
    font-size: 27px;
    letter-spacing: 4px;
    fill: var(--ink);
  }
  .brand-tagline {
    font-family: "Antonio", sans-serif;
    font-size: 10px;
    letter-spacing: 2px;
    fill: var(--ink);
  }
  .volume {
    font-family: "Jost", sans-serif;
    font-size: 11px;
    fill: var(--ink);
  }
</style>
</head>
<body>
<div class="canvas">
  <svg class="artwork" viewBox="0 0 1445 1445" preserveAspectRatio="none" xmlns="http://www.w3.org/2000/svg">
    <defs>
      <linearGradient id="gold-band" x1="0" y1="0" x2="1" y2="0">
        <stop offset="0" stop-color="var(--gold-mid)"/>
        <stop offset="0.2" stop-color="var(--gold-light)"/>
        <stop offset="0.55" stop-color="var(--gold-mid)"/>
        <stop offset="0.8" stop-color="var(--gold-deep)"/>
        <stop offset="0.95" stop-color="var(--gold-dark)"/>
      </linearGradient>
      <linearGradient id="gold-rim" x1="0" y1="0" x2="1" y2="1">
        <stop offset="0" stop-color="var(--gold-mid)"/>
        <stop offset="0.4" stop-color="var(--gold-light)"/>
        <stop offset="0.7" stop-color="var(--gold-deep)"/>
        <stop offset="1" stop-color="var(--gold-dark)"/>
      </linearGradient>
      <clipPath id="shield-inner">
        <path d="M122,466 Q440,266 793,466 Q752,848 455,1126 Q158,848 122,466 Z"/>
      </clipPath>
    </defs>

    <g class="recipe-label">
      <rect class="leaf-area" role="img" aria-label="Green manuka leaf ornament behind the shield" x="172" y="880" width="572" height="230" rx="24" fill="var(--leaf)"/>
      <path class="shield-edge" d="M108,460 Q440,246 807,460 Q764,856 455,1142 Q146,856 108,460 Z" fill="var(--peach)"/>
      <path class="shield-rim" d="M116,463 Q440,256 799,463 Q758,852 455,1134 Q152,852 116,463 Z" fill="url(#gold-rim)"/>
      <path class="shield-field" d="M122,466 Q440,266 793,466 Q752,848 455,1126 Q158,848 122,466 Z" fill="var(--peach)"/>
      <polygon class="gold-band" clip-path="url(#shield-inner)" points="100,490 620,378 820,430 820,535 100,705" fill="url(#gold-band)"/>

      <text class="recipe-title" x="475" y="553" text-anchor="middle">RECIPE<tspan class="hash">#</tspan>3</text>

      <g class="tasting-note" text-anchor="middle">
        <text x="457" y="703">A CLASSICALLY INSPIRED GIN</text>
        <text x="457" y="739">WITH DEVELOPED CITRUSNOTES FROM</text>
        <text x="457" y="776">THE MANUKABERRIES FROM CALLUM´S</text>
        <text x="457" y="812">MATES, BEST WITH A EQUAL</text>
        <text x="457" y="849">MIX OF SOME FANDY TONIC</text>
      </g>

      <text class="proof" x="457" y="915" text-anchor="middle">84 PROOF</text>
      <text class="abv-figure" x="458" y="1004" text-anchor="middle">42%</text>
      <text class="abv-caption" x="460" y="1033" text-anchor="middle">ALCOOL</text>
      <text class="abv-caption" x="460" y="1064" text-anchor="middle">BY VOL.</text>
    </g>

    <g class="main-label">
      <rect x="928" y="656" width="252" height="184" fill="var(--peach)"/>
      <path class="main-frame" d="M950,668 H1158 Q1158,680 1168,680 V822 Q1158,822 1158,832 H950 Q950,822 940,822 V680 Q950,680 950,668 Z" fill="none" stroke="url(#gold-rim)" stroke-width="3"/>
      <text class="brand-name" x="1054" y="748" text-anchor="middle">WANDERLARK</text>
      <line x1="958" y1="758" x2="1150" y2="758" stroke="var(--leaf)" stroke-width="1.5"/>
      <line x1="958" y1="776" x2="1150" y2="776" stroke="var(--leaf)" stroke-width="1.5"/>
      <text class="brand-tagline" x="1054" y="771" text-anchor="middle">NEW ZEALAND SMALL BATCH GIN</text>
      <text class="volume" x="1108" y="822">500ML</text>
    </g>
  </svg>
</div>
</body>
</html>
```